Create a banner for me that embodies my health and well being package.

I am an intuitive counselor with a busy practice helping clients to shift their blocks and move forward in their lives.
I have created a package called '9 paths home again'
I am wanting a banner to put on my website page, facebook page and to use as a letter head in mailouts.
My ideal clients are those who want to create change in their lives and who invest money in themselves and their personal and spiritual growth.
I am different to regular life coaches as my sessions have a spiritual twist to them creating much deeper change in my clients.
I would like the banner to be mainly font with the title of the progam: 9 Paths Home Again (no other wording) (something along the lines of the Blackjack font) and that ties in with the theme of my website. I'm not sure what else I want with it and am looking for ideas.
Website:
www.quillorabalancecare.com.au
I also have a current facebook page for the business:
https://www.facebook.com/Quillora-Balance-Care-402715938846102/
(Note: I am about to drop my logo and business name and move to using my own name - the rest of the website will remain the same).
I have attached a doc with the draft of what wording will be on the website page any advertising will link to, to give you an idea of what the program is about.

Target Market(s)

People who invest money on themselves who are looking to improve their emotional well being and creating change in their life. Majority are middle aged women (also younger females and some men)

Industry/Entity Type

Health And Wellness

Font styles to use
Other font styles liked:
• I like Blackjack and Amienne. Along those lines.

Requirements
Must have
• Attractive, modern and GREAT font.
Nice to have
• Surprise me with something amazing!
• I love the colours in the 2 images I have up loaded as they represent the heart chakra colours. They could be a feature on the banner or blurred into the background.
Should not have
• Even though my work is quite spiritual I don't want it to look woo woo (meaning airy fairy spiritual stuff!)

```html
<!DOCTYPE html>
<html lang="en">
<head>
<meta charset="utf-8">
<title>9 Paths Home Again – Quillora Balance Care</title>
<link rel="stylesheet" href="https://fonts.googleapis.com/css2?family=Anton&family=Varela+Round&family=Ubuntu:wght@500;700&family=Questrial&display=swap">
<style>
  :root {
    --stage: #e6ebe1;
    --paper: #ffffff;
    --lavender: #6b69a5;
    --sage: #a8c49b;
    --footer: #232323;
    --footer-text: #d9d9d9;
    --pink: #e2169b;
    --green: #2f8a2a;
  }
  * { box-sizing: border-box; margin: 0; padding: 0; }
  html, body { width: 1200px; height: 758px; overflow: hidden; background: var(--stage); }
  .page { position: absolute; left: 287px; top: 0; width: 629px; height: 758px; overflow: hidden; background: var(--paper); font-family: "Questrial", sans-serif; }

  .brand { position: absolute; left: 0; right: 0; top: 0; height: 100px; text-align: center; }
  .brand-mark { position: absolute; left: 280px; top: 2px; width: 66px; height: 66px; border-radius: 50%; background: var(--sage); }
  .brand-name { position: absolute; left: 0; right: 0; top: 72px; font-family: "Varela Round", sans-serif; font-size: 15px; color: var(--lavender); letter-spacing: 0.5px; }

  .hero { position: absolute; left: 12px; top: 104px; width: 604px; height: 227px; overflow: hidden; }
  .hero-backdrop { position: absolute; inset: 0;
    background: linear-gradient(90deg, var(--green) 0%, #c7a12c 22%, var(--pink) 40%, var(--pink) 60%, #c7a12c 78%, var(--green) 100%); }
  .main-nav { position: absolute; left: 0; top: 0; width: 100%; height: 34px; background: #000; display: flex; justify-content: space-between; padding: 7px 24px 0 26px; }
  .main-nav a { color: #fff; text-decoration: none; font-family: "Varela Round", sans-serif; font-size: 10px; line-height: 11px; }
  .hero-seal { position: absolute; left: 206px; top: 28px; width: 192px; height: 192px; border-radius: 50%; background: #000; color: #fff; text-align: center; }
  .hero-title { font-family: "Anton", sans-serif; font-weight: 400; line-height: 1; margin-top: 42px; letter-spacing: -0.5px; }
  .hero-title .big { display: block; font-size: 46px; }
  .hero-title .small { display: block; font-size: 29px; margin-top: 2px; }
  .hero-rule { width: 118px; height: 3px; background: var(--pink); margin: 9px auto 0; }

  .services { position: absolute; left: 15px; top: 344px; width: 600px; height: 178px; }
  .service { position: absolute; top: 0; width: 187px; height: 178px; background: var(--lavender); color: #fff; text-align: center; }
  .service:nth-child(1) { left: 0; }
  .service:nth-child(2) { left: 206px; }
  .service:nth-child(3) { left: 412px; }
  .service-photo { height: 96px; }
  .photo-pebbles { background: linear-gradient(135deg, #c7ccd8, #8e95a6 60%, #d4d6dd); }
  .photo-lily { background: linear-gradient(180deg, #2a3a2c 0%, #7a3556 50%, #151515 100%); }
  .photo-petals { background: linear-gradient(180deg, #8d8790 0%, #6e6670 55%, #b98a6d 80%, #8a5a4a 100%); }
  .service-title { font-family: "Varela Round", sans-serif; font-weight: 400; font-size: 15px; line-height: 18px; margin-top: 7px; }
  .service-rule { width: 30px; height: 1px; background: #fff; margin: 6px auto 5px; }
  .service-text { font-family: "Varela Round", sans-serif; font-size: 8px; line-height: 13.5px; }

  .newsletter { position: absolute; left: 0; top: 542px; width: 629px; height: 72px; background: var(--sage); }
  .newsletter-title { position: absolute; left: 50px; top: 15px; font-family: "Ubuntu", sans-serif; font-weight: 700; font-size: 12px; color: #fff; }
  .field { position: absolute; top: 41px; width: 219px; height: 15px; background: #fff; font-size: 7px; color: #aaa; padding: 4px 9px; }
  .field-name { left: 14px; }
  .field-email { left: 245px; }
  .signup-button { position: absolute; left: 483px; top: 7px; width: 55px; height: 55px; border-radius: 50%; background: #fff; color: var(--sage); font-family: "Ubuntu", sans-serif; font-weight: 500; font-size: 11px; line-height: 14px; text-align: center; padding-top: 13px; }

  .motto { position: absolute; left: 0; top: 614px; width: 629px; height: 37px; background: var(--lavender); color: #fff; font-family: "Ubuntu", sans-serif; font-weight: 500; font-size: 16px; letter-spacing: 3.5px; text-align: center; line-height: 37px; }

  .site-footer { position: absolute; left: 0; top: 651px; width: 629px; height: 107px; background: var(--footer); color: var(--footer-text); }
  .footer-col { position: absolute; top: 12px; }
  .footer-col h3 { font-family: "Varela Round", sans-serif; font-weight: 400; font-size: 10px; line-height: 12px; color: #fff; margin-bottom: 6px; }
  .footer-col p, .footer-col li { font-size: 7px; line-height: 10px; list-style: none; }
  .col-address { left: 18px; width: 260px; }
  .col-address h3.second { margin-top: 7px; }
  .col-locations { left: 280px; }
  .map-slot { width: 103px; height: 52px; background: linear-gradient(135deg, #eef0ea, #d9e3d2); }
  .col-hours { left: 401px; width: 115px; }
  .col-hours p { margin-bottom: 6px; }
  .col-menu { left: 523px; }
</style>
</head>
<body>
  <div class="page">
    <header class="brand">
      <div class="brand-mark"></div>
      <div class="brand-name">quillora balance care</div>
    </header>

    <section class="hero">
      <div class="hero-backdrop" role="img" aria-label="Pink, gold and green heart chakra colour pattern behind the title"></div>
      <nav class="main-nav">
        <a href="#">home</a>
        <a href="#">consultations</a>
        <a href="#">workshops</a>
        <a href="#">about<br>rosalind</a>
        <a href="#">happy<br>clients</a>
        <a href="#">blog</a>
        <a href="#">contact</a>
      </nav>
      <div class="hero-seal">
        <h1 class="hero-title"><span class="big">9 PATHS</span><span class="small">HOME AGAIN</span></h1>
        <div class="hero-rule"></div>
      </div>
    </section>

    <section class="services">
      <article class="service">
        <div class="service-photo photo-pebbles" role="img" aria-label="Photo of pebbles arranged in a spiral"></div>
        <h2 class="service-title">consultations</h2>
        <div class="service-rule"></div>
        <p class="service-text">consultations to shift<br>the things that are<br>holding you back</p>
      </article>
      <article class="service">
        <div class="service-photo photo-lily" role="img" aria-label="Photo of a pink water lily above a pond"></div>
        <h2 class="service-title">workshops</h2>
        <div class="service-rule"></div>
        <p class="service-text">a range of<br>weekend workshops<br>to help you grow</p>
      </article>
      <article class="service">
        <div class="service-photo photo-petals" role="img" aria-label="Photo of a wooden bowl of dried rose petals"></div>
        <h2 class="service-title">make a booking</h2>
        <div class="service-rule"></div>
        <p class="service-text">book in with Rosalind<br>to create the change<br>you are looking for</p>
      </article>
    </section>

    <section class="newsletter">
      <p class="newsletter-title">sign up to our newsletter for wellbeing tips and upcoming workshops</p>
      <div class="field field-name">Name:</div>
      <div class="field field-email">Email:</div>
      <div class="signup-button">yes<br>thanks</div>
    </section>

    <div class="motto">shift - create - grow</div>

    <footer class="site-footer">
      <div class="footer-col col-address">
        <h3>Clinic Address</h3>
        <p>The Larchmont Healing Rooms<br>42 Orchard Lane, Elmhurst 3199, Melbourne Australia</p>
        <h3 class="second">Workshop Address</h3>
        <p>Greenway Studio 12 - 14 Linden Street, (Cnr Ash and Linden Streets)<br>Harwood 3140, Melbourne Australia</p>
      </div>
      <div class="footer-col col-locations">
        <h3>Locations</h3>
        <div class="map-slot" role="img" aria-label="Street map showing the clinic location"></div>
      </div>
      <div class="footer-col col-hours">
        <h3>Clinic Hours</h3>
        <p>Tuesdays 9am - 2pm</p>
        <p>Thursdays 9am - 2pm</p>
        <p>Wednesdays and evenings<br>Video call by appointment.</p>
      </div>
      <div class="footer-col col-menu">
        <h3>Menu</h3>
        <ul>
          <li>Home</li>
          <li>Consultations</li>
          <li>Workshops</li>
          <li>About Rosalind</li>
          <li>Happy Clients</li>
        </ul>
      </div>
    </footer>
  </div>
</body>
</html>
```